Rebrand of an existing product label

We are looking for a new design / label for our body lotion. Attached is the current product label. We have this product available in Retinol, Collagen, Hyaluronic Acid, Vitamin C, and Coconut. The brand should reflect a clinical, trustworthy look. We also want to include on the label that the product contains Dead Sea Minerals. Attached is the dieline for the label for the jar and the top. This jar is the packaging that needs to be used for this project.

Target Market(s)

40+

Requirements
Must have
• Ingredient callouts on the front + benefits. Ex- Vitamin C Brightening Cream

```html
<!DOCTYPE html>
<html lang="en">
<head>
<meta charset="utf-8">
<title>Vitamin C Body Lotion – Jar Label</title>
<link rel="stylesheet" href="https://fonts.googleapis.com/css2?family=Poppins:wght@300;400;600&display=swap">
<style>
  :root {
    --label-orange: #f29100;
    --ink-white: #ffffff;
    --ink-black: #111111;
    --page-bg: #ffffff;
  }
  html, body {
    margin: 0;
    padding: 0;
    width: 1200px;
    height: 800px;
    overflow: hidden;
    background: var(--page-bg);
  }
  .jar-label {
    display: block;
    width: 1200px;
    height: 800px;
  }
  .label-shape { fill: var(--label-orange); }
  .badge-frame {
    fill: none;
    stroke: var(--ink-white);
    stroke-width: 1.6;
  }
  .badge-icon { fill: var(--ink-white); }
  .badge-tick {
    fill: none;
    stroke: var(--label-orange);
    stroke-width: 2.2;
    stroke-linecap: round;
    stroke-linejoin: round;
  }
  .badge-text {
    font-family: "Poppins", sans-serif;
    font-weight: 600;
    fill: var(--ink-white);
    text-anchor: middle;
  }
  .claim-line {
    font-family: "Poppins", sans-serif;
    font-weight: 300;
    font-size: 37px;
    fill: var(--ink-white);
    text-anchor: middle;
  }
  .rule {
    stroke: var(--ink-white);
    stroke-width: 1.8;
  }
  .ingredient-title {
    font-family: "Poppins", sans-serif;
    font-weight: 300;
    font-size: 168px;
    fill: var(--ink-white);
    text-anchor: middle;
  }
  .product-type {
    font-family: "Poppins", sans-serif;
    font-weight: 300;
    font-size: 47px;
    fill: var(--ink-black);
    text-anchor: middle;
  }
  .brand-name {
    font-family: "Poppins", sans-serif;
    font-weight: 300;
    font-size: 40px;
    letter-spacing: 6px;
    fill: var(--ink-black);
    text-anchor: middle;
  }
</style>
</head>
<body>
<svg class="jar-label" viewBox="0 0 923 615" xmlns="http://www.w3.org/2000/svg" role="img" aria-label="Vitamin C body lotion jar label">
  <path class="label-shape" d="M0,250 C0,110 70,10 170,5 C230,2 270,40 300,80 C340,135 400,165 461,165 C522,165 582,135 622,80 C652,40 692,2 752,5 C852,10 923,110 923,250 L923,330 C923,490 720,615 461,615 C202,615 0,490 0,330 Z"/>

  <g class="badge badge-derm">
    <rect class="badge-frame" x="81" y="25" width="125" height="130" rx="20"/>
    <path class="badge-icon" d="M143,48 C136,60 128,70 128,80 A15,15 0 0 0 158,80 C158,70 150,60 143,48 Z"/>
    <polyline class="badge-tick" points="136,80 141,85 150,75"/>
    <text class="badge-text" x="143" y="118" font-size="11.5">DERMATOLOGICALLY</text>
    <text class="badge-text" x="143" y="134" font-size="11.5">TESTED</text>
  </g>

  <g class="badge badge-lab">
    <rect class="badge-frame" x="720" y="25" width="125" height="130" rx="20"/>
    <path class="badge-icon" d="M775,50 L789,50 L789,54 L786,54 L786,68 L799,95 Q801,100 795,100 L769,100 Q763,100 765,95 L778,68 L778,54 L775,54 Z"/>
    <polyline class="badge-tick" points="775,86 780,91 789,81"/>
    <text class="badge-text" x="782" y="122" font-size="13.5">LABORATORY</text>
    <text class="badge-text" x="782" y="140" font-size="13.5">TESTED</text>
  </g>

  <text class="claim-line" x="461.5" y="222" textLength="697" lengthAdjust="spacingAndGlyphs">EX- VITAMIN C BRIGHTENING CREAM</text>
  <line class="rule" x1="117" y1="242" x2="805" y2="242"/>

  <text class="ingredient-title" x="459" y="379" textLength="752" lengthAdjust="spacingAndGlyphs">VITAMIN C</text>
  <line class="rule" x1="117" y1="402" x2="805" y2="402"/>

  <text class="product-type" x="461" y="461" textLength="315" lengthAdjust="spacingAndGlyphs">BODY LOTION</text>

  <text class="brand-name" x="461" y="548">SOLENNE</text>
</svg>
</body>
</html>
```